Harborline Wealth
Harborline Wealth Partners, LLC
Harborline Wealth - Financial Services
Creative Brief
Financial Services
Harborline Wealth Partners, LLC is a Michigan-based financial planning firm. We have comprehensive knowledge of strategies for Harborline Wealth. At Harborline Wealth Partners we focus on helping retirees and those preparing for retirement to maximize their finances throughout their semi-retired and non-working years.
left side
Cobaltview Advisory Group in Maryland
I want my website to model Cobaltview Advisory Group in Maryland. I want similar language and I want those colors.
minkovel minkovel
Hi Designers, Logo Vector File uploaded. Thanks,
I am trying to get my logo posted. Thanks Todd

```html
<!DOCTYPE html>
<html lang="en">
<head>
<meta charset="utf-8">
<title>Harborline Wealth Partners, LLC</title>
<link href="https://fonts.googleapis.com/css2?family=Figtree:ital,wght@0,400;0,600;0,700;1,400&family=Rajdhani:wght@500;600&display=swap" rel="stylesheet">
<style>
  :root {
    --green: #0a7a48;
    --green-dark: #0b5a2b;
    --gold: #d1aa2c;
    --gold-text: #9b7d1c;
    --ink: #3a3a3a;
    --grey-bg: #f3f3f3;
    --footer: #333333;
    --footer-base: #1d1d1d;
    --rule: #cfcfcf;
  }
  * { box-sizing: border-box; margin: 0; padding: 0; }
  html, body { width: 840px; height: 1200px; overflow: hidden; }
  body { position: relative; background: #fff; font-family: "Figtree", sans-serif; color: var(--ink); }
  .abs { position: absolute; }

  /* header */
  .site-header { left: 0; top: 0; width: 840px; height: 101px; background: #fff; border-bottom: 1px solid #e2e2e2; }
  .brand { left: 92px; top: 38px; font-size: 19px; font-weight: 700; color: var(--green); white-space: nowrap; }
  .consult-btn { left: 475px; top: 16px; width: 126px; height: 30px; border-radius: 2px;
    background: linear-gradient(#3aa867, #0b6f3c); color: #fff; text-align: center;
    font-size: 10px; line-height: 12px; padding-top: 3px; font-weight: 600; }
  .consult-btn b { display: block; font-weight: 700; font-size: 10.5px; }
  .phone-icon { left: 614px; top: 20px; width: 21px; height: 21px; border-radius: 3px; background: linear-gradient(#f1d690, #d6ab47); }
  .phone-number { left: 643px; top: 20px; font-size: 16px; color: #333; letter-spacing: .3px; }

  /* hero */
  .hero { left: 0; top: 102px; width: 840px; height: 359px; background: linear-gradient(135deg, #f6f6f6, #e3e4e6); }
  .hero-media { left: 102px; top: 9px; width: 640px; height: 290px;
    background: linear-gradient(90deg, #f3efe2, #e9dcae); }
  .hero-name { left: 0; top: 186px; width: 840px; text-align: center; font-size: 36px; font-weight: 700; color: var(--green); white-space: nowrap; }
  .hero-btn { left: 371px; top: 285px; width: 97px; height: 29px; border-radius: 15px; background: var(--green-dark);
    border: 2px solid #fff; box-shadow: 0 0 0 1px #bbb; color: #fff; font-size: 13px; font-weight: 600; text-align: center; line-height: 25px; }
  .dots { left: 92px; top: 333px; display: flex; gap: 5px; }
  .dots span { width: 8px; height: 8px; border-radius: 50%; background: #a8a8a8; }
  .dots span.on { background: var(--green-dark); }

  /* intro */
  .intro-title { left: 0; top: 490px; width: 840px; text-align: center; font-family: "Rajdhani", sans-serif; font-size: 20px; font-weight: 500; color: var(--green); }
  .intro-title small { font-size: 12px; color: #666; margin-left: 4px; }
  .intro-lead { left: 0; top: 528px; width: 840px; text-align: center; font-size: 15px; }
  .intro-text { left: 110px; top: 560px; width: 620px; text-align: center; font-size: 10px; line-height: 16px; }
  .gold-btn { background: var(--gold); color: #fff; font-weight: 700; font-size: 10px; text-align: center; border-radius: 1px; }
  .intro-btn { left: 383px; top: 611px; width: 73px; height: 21px; line-height: 21px; }

  /* columns */
  .columns { left: 0; top: 657px; width: 840px; height: 353px; background: var(--grey-bg); border-top: 1px solid #e2e2e2; }
  .col-title { top: 683px; width: 197px; font-family: "Rajdhani", sans-serif; font-size: 18px; font-weight: 500; color: #333;
    border-bottom: 1px dotted #888; padding-bottom: 2px; }
  .col-title em { font-style: normal; color: var(--green); }
  .col-sep { top: 682px; width: 1px; height: 204px; background: #e0e0e0; }
  .news-date { left: 552px; font-size: 9px; font-weight: 700; color: var(--green); }
  .news-link { left: 552px; font-size: 8.5px; font-weight: 700; color: var(--gold-text); text-decoration: underline; }
  .news-text { left: 552px; width: 197px; font-size: 8.5px; line-height: 13px; }
  .news-text span { color: var(--green); }
  .news-rule { left: 552px; width: 197px; border-top: 1px dotted #bbb; }
  .info-btn { left: 551px; top: 871px; width: 110px; height: 21px; line-height: 21px; }

  /* footer */
  .footer-curve { left: 0; top: 840px; }
  .footer-body { left: 0; top: 1010px; width: 840px; height: 160px; background: var(--footer); }
  .foot-title { top: 1027px; width: 168px; color: #fff; font-size: 11px; font-weight: 600; border-bottom: 1px solid #454545; padding-bottom: 8px; }
  .foot-text { left: 93px; top: 1062px; width: 170px; color: #ddd; font-size: 8.5px; line-height: 13px; }
  .email { left: 92px; top: 1091px; width: 167px; height: 23px; background: #fff; border-radius: 2px; font-size: 8.5px; font-style: italic; color: #888; padding: 6px 6px; }
  .subscribe { left: 92px; top: 1122px; width: 73px; height: 22px; line-height: 22px; font-size: 8.5px; }
  .foot-sep { top: 1055px; width: 1px; height: 90px; background: #2a2a2a; }
  .map-box { left: 583px; top: 1054px; width: 168px; height: 96px; border: 1px solid #777; }
  .copyright { left: 0; top: 1170px; width: 840px; height: 30px; background: var(--footer-base); color: #ccc; font-size: 8.5px; text-align: center; line-height: 30px; }
</style>
</head>
<body>
  <header class="abs site-header">
    <div class="abs brand">Harborline Wealth Partners, LLC</div>
    <div class="abs consult-btn">Schedule a<b>FREE CONSULTATION</b></div>
    <div class="abs phone-icon">
      <svg width="21" height="21" viewBox="0 0 21 21"><path d="M7 5c1 0 1.5 2.5 1 3l-1 1c.7 1.8 2 3.2 4 4l1-1c.6-.5 3 0 3 1v2c0 .6-1 1-2 1-4 0-8-4-8-8 0-1 .4-2 1-2z" fill="#fff"/></svg>
    </div>
    <div class="abs phone-number">555-014-2290</div>
  </header>

  <section class="abs hero">
    <div class="abs hero-media" role="img" aria-label="Hero illustration of a gold suspension bridge"></div>
    <div class="abs hero-name">Harborline Wealth Partners, LLC</div>
    <div class="abs hero-btn">Read More</div>
    <div class="abs dots"><span class="on"></span><span></span><span></span><span></span></div>
  </section>

  <div class="abs intro-title">Harborline Wealth <small>Partners, LLC</small></div>
  <p class="abs intro-lead">We have comprehensive knowledge of strategies for Harborline Wealth.</p>
  <p class="abs intro-text">At Harborline Wealth Partners we focus on helping retirees and those preparing for retirement to maximize their finances throughout their semi-retired and non-working years.</p>
  <div class="abs gold-btn intro-btn">Read More ›</div>

  <section class="abs columns"></section>
  <h2 class="abs col-title" style="left:93px"><em>Hot</em> Topics</h2>
  <div class="abs col-sep" style="left:304px"></div>
  <h2 class="abs col-title" style="left:321px"><em>2015 Workshop</em> Schedule</h2>
  <div class="abs col-sep" style="left:534px"></div>
  <h2 class="abs col-title" style="left:552px"><em>Latest</em> News</h2>

  <div class="abs news-date" style="top:721px">01.01.2015</div>
  <div class="abs news-link" style="top:740px">Duis autem vel eum iriure dolor in hendreritm</div>
  <p class="abs news-text" style="top:758px">Ut wisi enim ad minim veniam, quis nostrud holi exerci tation ullamcorper consequat <span>[...]</span></p>
  <div class="abs news-rule" style="top:790px"></div>
  <div class="abs news-date" style="top:795px">01.01.2015</div>
  <div class="abs news-link" style="top:814px">Duis autem vel eum iriure dolor in hendreritm</div>
  <p class="abs news-text" style="top:832px">Ut wisi enim ad minim veniam, quis nostrud holi exerci tation ullamcorper consequat <span>[...]</span></p>
  <div class="abs gold-btn info-btn">Request More Info ›</div>

  <svg class="abs footer-curve" width="840" height="171" viewBox="0 0 840 171">
    <defs>
      <linearGradient id="band" x1="0" x2="1" y1="0" y2="0">
        <stop offset="0" stop-color="#fbf3dc"/>
        <stop offset="1" stop-color="#d8b548"/>
      </linearGradient>
    </defs>
    <path d="M0,116 C200,168 560,140 840,8 L840,24 C560,150 200,176 0,130 Z" fill="url(#band)"/>
    <path d="M0,130 C200,176 560,150 840,24 L840,171 L0,171 Z" fill="#333333"/>
  </svg>
  <div class="abs footer-body"></div>
  <div class="abs foot-title" style="left:93px">Newsletter Sign Up</div>
  <div class="abs foot-title" style="left:339px">Contact Information</div>
  <div class="abs foot-title" style="left:585px">Location</div>
  <p class="abs foot-text">Lorem ipsudolor sit coec adipiscingmop elitsite amet</p>
  <div class="abs email">Email Address</div>
  <div class="abs gold-btn subscribe">SUBSCRIBE</div>
  <div class="abs foot-sep" style="left:297px"></div>
  <div class="abs foot-sep" style="left:543px"></div>
  <div class="abs map-box" role="img" aria-label="Office location map"></div>
  <div class="abs copyright">© 2014 Harborline llc. All Rights Reserved.</div>
</body>
</html>
```